Environmental Plastics Infographic on Marine Debris

We need a series of infographics that can be used individually or as a combined presentation. We'd like the combined piece to include an introduction and conclusion along with 4-5 infographics. Each infographic (information unit) should also work as a standalone. We are trying to help people visualize size proportions and ratios to put the plastics marine debris problem in perspective. Our key point is concerning polystyrene foam which represents 35 tons. We are looking for something creative to help people understand what the problem represents in terms they are familiar with.

To view our typical company design/style please see our website at www.harbenfoamworks.org. Our primary RGB colors are: (187,140,9); (94,47,29); (94,138,164); and (164,167,15). Secondary RGB colors are (249,162,28) and (218,210,208). Our title/header font is DIN Next LT Pro and our copy font is Calibri 10.5 pt. We can deviate from the font specification if beneficial and welcome interesting text treatments and typography.

Need extra days to review

Target Market(s)

international brand manufacturers (brenloch, tavix), US legislators & government agencies

Font styles to use
Sans Serif

Requirements
Must have
• Sufficient white space. Easy to grasp message concept with visual components.

```html
<!DOCTYPE html>
<html lang="en">
<head>
<meta charset="utf-8">
<title>How Will Polystyrene Bans Improve Ocean Health?</title>
<link href="https://fonts.googleapis.com/css2?family=Oswald:wght@500;600&family=Carlito:wght@400;700&display=swap" rel="stylesheet">
<style>
:root{
  --olive:#a4a70f;
  --olive-dark:#8d900c;
  --brown:#5e2f1d;
  --blue:#5e8aa4;
  --gold:#bb8c09;
  --orange:#f9a21c;
  --grey:#dad2d0;
  --canvas:#fbe2b3;
  --ink:#2b2b2b;
  --ink-dark:#1e1e1e;
  --white:#ffffff;
}
*{box-sizing:border-box;margin:0;padding:0}
html,body{width:792px;height:1200px;overflow:hidden;background:var(--canvas)}
body{position:relative;font-family:'Carlito',Calibri,sans-serif;color:var(--ink)}
.panel{position:absolute;background:var(--white);overflow:hidden;box-shadow:0 1px 3px rgba(0,0,0,.15)}
.panel-head{background:var(--olive);color:var(--white);font-family:'Oswald',sans-serif;font-weight:600;text-align:center;text-transform:uppercase;display:flex;align-items:center;justify-content:center;line-height:1.12}
.abs{position:absolute}
.ph{position:absolute;border-radius:3px}
.num{color:var(--olive);font-weight:700}
.gold{color:var(--orange)}
.copy{font-size:6.2px;line-height:1.35;color:var(--ink)}
.tick{display:inline-block;vertical-align:middle}
.stat{margin-top:6px;line-height:1.25}
.stat b{font-weight:700}
.label-small{font-size:5.4px;color:var(--blue);text-align:center}
.tons{font-family:'Oswald',sans-serif;color:var(--orange);font-size:9px;font-weight:500}
.divider-v{position:absolute;border-left:1px dashed var(--olive)}
.divider-h{position:absolute;border-top:1px dashed var(--olive)}
.bubble{position:absolute;border-radius:50%;display:flex;flex-direction:column;align-items:center;justify-content:center;text-align:center;color:var(--white)}
.bubble .cap{font-family:'Carlito',sans-serif;font-weight:700;font-size:6.4px;line-height:1.15}
.bubble .val{font-family:'Oswald',sans-serif;font-size:9.5px;font-weight:500;margin-top:2px}
.size-row{position:absolute;left:0;width:381px;height:28px;border-bottom:1px dashed rgba(255,255,255,.7);font-family:'Oswald',sans-serif;color:var(--white);font-size:10px}
.bag{position:absolute;background:var(--ink-dark);border-radius:45% 45% 40% 40%;color:var(--orange);font-family:'Oswald',sans-serif;display:flex;align-items:center;justify-content:center}
.find{display:flex;align-items:center;gap:10px;font-size:9.2px;margin-bottom:13px}
.bells{position:absolute;display:flex;flex-wrap:wrap;gap:2px 3px;overflow:hidden}
</style>
</head>
<body>
<svg width="0" height="0" style="position:absolute">
  <symbol id="kettlebell" viewBox="0 0 20 22">
    <path d="M5 8 V4 a5 4 0 0 1 10 0 V8" fill="none" stroke="#1e1e1e" stroke-width="2.4"/>
    <circle cx="10" cy="14" r="7.5" fill="#1e1e1e"/>
    <circle cx="10" cy="14.5" r="4.2" fill="#f9a21c"/>
    <text x="10" y="16.6" font-size="5.2" text-anchor="middle" font-family="Oswald,sans-serif" fill="#1e1e1e">50</text>
  </symbol>
  <symbol id="check" viewBox="0 0 20 20">
    <circle cx="10" cy="10" r="10" fill="#5e8aa4"/>
    <path d="M5.5 10.3 l3 3 l6-6.5" fill="none" stroke="#fff" stroke-width="2"/>
  </symbol>
</svg>

<!-- Intro, wide layout -->
<section class="panel" style="left:10px;top:12px;width:381px;height:286px">
  <div class="panel-head" style="height:104px;font-size:29px">How will polystyrene bans<br>improve ocean health?</div>
  <div class="copy" style="padding:12px 16px 0">
    A recent <span style="color:var(--blue);text-decoration:underline">report</span> looks at the role plastics play in marine debris that sheds light on previous assumptions about how different plastics contribute to the problem and where its coming from.<br>
    In this ground breaking study, scientists conducted cutting-edge research at a much larger scale than had ever been done before. Over the course of three years, an international team including The Open Sea Survey Foundation, six universities, and an aerial sensor company, collected data and mapped debris fields for the Great Pacific Garbage Patch, one of the most problematic plastic pollution hot spots.<br>
    Polystyrene ban legislation imply product restrictions will minimize plastic marine debris. Let's take a closer look.
  </div>
  <div class="abs" style="left:0;top:196px;width:381px;height:90px;background:var(--grey);padding:12px 20px 0;font-size:6.3px">
    <div>The total plastics mass in the GPGP is projected at <span class="num" style="font-size:10px;color:var(--gold)">78,908 tons.</span></div>
    <div class="stat"><svg class="tick" width="9" height="9"><use href="#check"/></svg> <span class="num" style="font-size:10px">52%</span> is mostly <b>abandoned fishing gear</b>, not consumer plastics.</div>
    <div class="stat"><svg class="tick" width="9" height="9"><use href="#check"/></svg> <span class="num" style="font-size:10px">47%</span> is <b>hard plastics, sheets and film</b>, making up the majority of the microplastics mass.</div>
    <div class="stat"><svg class="tick" width="9" height="9"><use href="#check"/></svg> <span class="num" style="font-size:10px">0,05%</span> is <b>foamed plastics</b> – including polystyrene – making it a minor component of the GPGP.</div>
  </div>
</section>

<!-- Intro, column layout -->
<section class="panel" style="left:402px;top:12px;width:382px;height:286px">
  <div class="panel-head" style="height:108px;font-size:29px">How will polystyrene bans<br>improve ocean health?</div>
  <div class="copy" style="position:absolute;left:14px;top:120px;width:136px;text-align:justify;font-size:5.9px;line-height:1.32">
    A recent report looks at the role plastics play in marine debris that sheds light on previous assumptions about how different plastics contribute to the problem and where its coming from.<br>
    In this ground breaking study, scientists conducted cutting-edge research at a much larger scale than had ever been done before.<br>
    Over the course of three years, an international team including The Open Sea Survey Foundation, six universities, and an aerial sensor company, collected data and mapped debris fields for the Great Pacific Garbage Patch, one of the most problematic plastic pollution hot spots.<br>
    Polystyrene ban legislation imply product restrictions will minimize plastic marine debris. Let's take a closer look.
  </div>
  <div class="abs" style="left:161px;top:108px;width:221px;height:178px;background:var(--grey);padding:18px 10px 0;font-size:7.6px">
    <div>The total plastics mass in the GPGP is projected at</div>
    <div class="num" style="font-size:14px;color:var(--gold)">78,908 tons.</div>
    <div class="stat" style="margin-top:9px"><svg class="tick" width="12" height="12"><use href="#check"/></svg> <span class="num" style="font-size:13px">52%</span> is mostly <b>abandoned fishing gear</b>, not consumer plastics.</div>
    <div class="stat" style="margin-top:9px"><svg class="tick" width="12" height="12"><use href="#check"/></svg> <span class="num" style="font-size:13px">47%</span> is <b>hard plastics, sheets and film</b>, making up the majority of the microplastics mass.</div>
    <div class="stat" style="margin-top:9px"><svg class="tick" width="12" height="12"><use href="#check"/></svg> <span class="num" style="font-size:13px">0,05%</span> is <b>foamed plastics</b> – including polystyrene – making it a minor component of the GPGP.</div>
  </div>
</section>

<!-- How big, wide -->
<section class="panel" style="left:10px;top:309px;width:381px;height:285px">
  <div class="panel-head" style="height:39px;font-size:24px;text-transform:none">How Big is BIG?</div>
  <div class="abs" style="left:0;top:39px;width:381px;height:96px">
    <div class="abs" style="left:0;top:52px;width:381px;height:44px;background:var(--olive)"></div>
    <div class="abs" style="left:32px;top:8px;font-size:6.6px;font-weight:700">1 Cruise Ship<br><span class="gold" style="font-weight:400">100,000 tons</span></div>
    <div class="ph" role="img" aria-label="Cruise ship illustration" style="left:26px;top:30px;width:72px;height:30px;background:linear-gradient(#e8ecef,#7d8a95)"></div>
    <div class="abs" style="left:166px;top:8px;font-size:6.6px;font-weight:700">1 Blue Whale<br><span class="gold" style="font-weight:400">150,000 tons</span></div>
    <div class="ph" role="img" aria-label="Blue whale illustration" style="left:136px;top:30px;width:102px;height:24px;border-radius:50%;background:linear-gradient(#8fb0c4,#5e8aa4)"></div>
    <div class="abs" style="left:270px;top:8px;font-size:6.6px;font-weight:700">1 Week NYC Waste Generation<br><span class="gold" style="font-weight:400;margin-left:28px">269,230 tons</span></div>
    <div class="ph" role="img" aria-label="City skyline with garbage truck" style="left:258px;top:24px;width:115px;height:40px;background:linear-gradient(#c9a98d,#4d5560)"></div>
    <div class="abs" style="left:28px;top:75px;color:#fff;font-size:8px;font-weight:700">GPGP = 79%</div>
    <div class="abs" style="left:146px;top:75px;color:#fff;font-size:8px;font-weight:700">GPGP = 53%</div>
    <div class="abs" style="left:298px;top:75px;color:#fff;font-size:8px;font-weight:700">GPGP = 29%</div>
  </div>
  <div class="abs" style="left:0;top:135px;width:381px;height:4px;background:var(--brown)"></div>
  <div class="divider-v" style="left:89px;top:150px;height:130px"></div>
  <div class="divider-v" style="left:170px;top:150px;height:130px"></div>
  <div class="divider-v" style="left:269px;top:150px;height:130px"></div>
  <div class="ph" role="img" aria-label="Pile of garbage patch plastics" style="left:22px;top:160px;width:48px;height:16px;background:linear-gradient(#9fb3c2,#3f4d5a)"></div>
  <div class="abs label-small" style="left:0;top:184px;width:89px">All GPGP Plastics</div>
  <div class="abs tons" style="left:0;top:212px;width:89px;text-align:center">78,908 tons</div>
  <div class="ph" role="img" aria-label="Cruise ship" style="left:110px;top:155px;width:40px;height:22px;background:linear-gradient(#e8ecef,#7d8a95)"></div>
  <div class="abs label-small" style="left:89px;top:184px;width:81px">1 Cruise Ship</div>
  <div class="abs tons" style="left:89px;top:212px;width:81px;text-align:center">100,000 tons</div>
  <div class="ph" role="img" aria-label="Blue whale" style="left:196px;top:162px;width:56px;height:12px;border-radius:50%;background:linear-gradient(#8fb0c4,#5e8aa4)"></div>
  <div class="abs label-small" style="left:170px;top:184px;width:99px">1 Blue Whale</div>
  <div class="abs tons" style="left:170px;top:212px;width:99px;text-align:center">200,000 tons</div>
  <div class="ph" role="img" aria-label="City skyline" style="left:296px;top:155px;width:50px;height:22px;background:linear-gradient(#c9a98d,#4d5560)"></div>
  <div class="abs label-small" style="left:269px;top:184px;width:112px">1 Week NYC City Waste Generation</div>
  <div class="abs tons" style="left:269px;top:212px;width:112px;text-align:center">269,230 tons</div>
  <div class="bells" style="left:24px;top:236px;width:28px;height:20px;flex-wrap:nowrap"><svg width="17" height="19" style="flex:none"><use href="#kettlebell"/></svg><svg width="17" height="19" style="flex:none"><use href="#kettlebell"/></svg></div>
  <div class="bells" style="left:112px;top:236px"><svg width="17" height="19"><use href="#kettlebell"/></svg><svg width="17" height="19"><use href="#kettlebell"/></svg></div>
  <div class="bells" style="left:176px;top:236px;gap:2px"><svg width="21" height="19"><use href="#kettlebell"/></svg><svg width="21" height="19"><use href="#kettlebell"/></svg><svg width="21" height="19"><use href="#kettlebell"/></svg><svg width="21" height="19"><use href="#kettlebell"/></svg></div>
  <div class="bells" style="left:274px;top:236px;width:107px;height:20px;flex-wrap:nowrap;gap:2px"><svg width="21" height="19" style="flex:none"><use href="#kettlebell"/></svg><svg width="21" height="19" style="flex:none"><use href="#kettlebell"/></svg><svg width="21" height="19" style="flex:none"><use href="#kettlebell"/></svg><svg width="21" height="19" style="flex:none"><use href="#kettlebell"/></svg><svg width="21" height="19" style="flex:none"><use href="#kettlebell"/></svg></div>
</section>

<!-- How big, column -->
<section class="panel" style="left:402px;top:309px;width:382px;height:285px">
  <div class="panel-head" style="height:39px;font-size:24px;text-transform:none">How Big is BIG?</div>
  <div class="abs" style="left:195px;top:39px;width:3px;height:246px;background:var(--olive)"></div>
  <div class="ph" role="img" aria-label="Cruise ship" style="left:8px;top:60px;width:76px;height:34px;background:linear-gradient(#e8ecef,#7d8a95)"></div>
  <div class="abs" style="left:26px;top:112px;font-size:6.6px;color:var(--blue)">GPGP = 79%</div>
  <div class="abs" style="left:94px;top:80px;width:90px;text-align:center;font-family:'Oswald',sans-serif;font-size:9px">1 Cruise Ship<br><span class="gold">100,000 tons</span></div>
  <div class="divider-h" style="left:10px;top:125px;width:175px;border-top-style:solid;border-color:#ccc"></div>
  <div class="ph" role="img" aria-label="Blue whale" style="left:8px;top:138px;width:68px;height:40px;border-radius:50%;background:linear-gradient(#8fb0c4,#5e8aa4)"></div>
  <div class="abs" style="left:26px;top:186px;font-size:6.6px;color:var(--blue)">GPGP = 53%</div>
  <div class="abs" style="left:94px;top:156px;width:90px;text-align:center;font-family:'Oswald',sans-serif;font-size:9px">1 Blue Whale<br><span class="gold">150,000 tons</span></div>
  <div class="divider-h" style="left:10px;top:198px;width:175px;border-top-style:solid;border-color:#ccc"></div>
  <div class="ph" role="img" aria-label="City skyline with garbage truck" style="left:4px;top:208px;width:80px;height:60px;background:linear-gradient(#c9a98d,#4d5560)"></div>
  <div class="abs" style="left:26px;top:274px;font-size:6.6px;color:var(--blue)">GPGP = 29%</div>
  <div class="abs" style="left:94px;top:218px;width:90px;text-align:center;font-family:'Oswald',sans-serif;font-size:8.4px;line-height:1.35">1 Week NYC Waste<br>Generation<br><span class="gold">269,230 tons</span></div>

  <div class="ph" role="img" aria-label="Pile of garbage patch plastics" style="left:210px;top:56px;width:48px;height:16px;background:linear-gradient(#9fb3c2,#3f4d5a)"></div>
  <div class="abs label-small" style="left:206px;top:76px">All GPGP Plastics</div>
  <div class="abs tons" style="left:270px;top:61px">78,908 tons</div>
  <div class="bells" style="left:326px;top:59px;width:28px;height:20px;flex-wrap:nowrap"><svg width="17" height="19" style="flex:none"><use href="#kettlebell"/></svg><svg width="17" height="19" style="flex:none"><use href="#kettlebell"/></svg></div>
  <div class="divider-h" style="left:205px;top:94px;width:168px"></div>
  <div class="ph" role="img" aria-label="Cruise ship" style="left:210px;top:102px;width:42px;height:22px;background:linear-gradient(#e8ecef,#7d8a95)"></div>
  <div class="abs label-small" style="left:210px;top:131px">1 Cruise Ship</div>
  <div class="abs tons" style="left:266px;top:110px">100,000 tons</div>
  <div class="bells" style="left:326px;top:108px;width:40px"><svg width="17" height="19"><use href="#kettlebell"/></svg><svg width="17" height="19"><use href="#kettlebell"/></svg></div>
  <div class="divider-h" style="left:205px;top:146px;width:168px"></div>
  <div class="ph" role="img" aria-label="Blue whale" style="left:208px;top:172px;width:54px;height:12px;border-radius:50%;background:linear-gradient(#8fb0c4,#5e8aa4)"></div>
  <div class="abs label-small" style="left:210px;top:190px">1 Blue Whale</div>
  <div class="abs tons" style="left:266px;top:170px">200,000 tons</div>
  <div class="bells" style="left:326px;top:156px;width:40px"><svg width="17" height="19"><use href="#kettlebell"/></svg><svg width="17" height="19"><use href="#kettlebell"/></svg><svg width="17" height="19"><use href="#kettlebell"/></svg><svg width="17" height="19"><use href="#kettlebell"/></svg></div>
  <div class="divider-h" style="left:205px;top:212px;width:168px"></div>
  <div class="ph" role="img" aria-label="City skyline" style="left:210px;top:228px;width:50px;height:24px;background:linear-gradient(#c9a98d,#4d5560)"></div>
  <div class="abs label-small" style="left:204px;top:260px;width:62px;line-height:1.2">1 Week NYC City<br>Waste Generation</div>
  <div class="abs tons" style="left:266px;top:242px">269,230 tons</div>
  <div class="bells" style="left:326px;top:222px;width:56px;height:42px"><svg width="17" height="19"><use href="#kettlebell"/></svg><svg width="17" height="19"><use href="#kettlebell"/></svg><svg width="17" height="19"><use href="#kettlebell"/></svg><svg width="17" height="19"><use href="#kettlebell"/></svg><svg width="17" height="19"><use href="#kettlebell"/></svg><svg width="17" height="19"><use href="#kettlebell"/></svg></div>
</section>

<!-- Sizing it up -->
<section class="panel" style="left:10px;top:606px;width:381px;height:285px">
  <div class="abs" style="left:0;top:124px;width:381px;height:161px;background:var(--olive)"></div>
  <div class="abs" style="left:14px;top:6px;width:118px;height:140px;background:var(--white);box-shadow:0 1px 4px rgba(0,0,0,.35);padding:5px">
    <div style="display:flex;align-items:center;gap:4px;font-weight:700;font-size:10px"><span style="display:inline-block;width:10px;height:10px;border-radius:50%;background:var(--ink-dark)"></span>Tidewater News</div>
    <div role="img" aria-label="Photo of sailors hauling plastic debris from the sea" style="margin-top:3px;height:58px;background:linear-gradient(#9bb2c4,#3d556a)"></div>
    <div style="font-family:Georgia,serif;font-weight:700;font-size:7.2px;line-height:1.12;margin-top:4px">Great Pacific Garbage Patch weighs more than 43,000 cars and is much larger than we thought</div>
    <div style="font-size:3px;color:#777;margin-top:3px">Posted March 2018 · Updated April 2018</div>
  </div>
  <div class="abs" style="left:180px;top:16px;font-family:'Oswald',sans-serif;font-size:8px;color:var(--orange)">Total GPGP Mass</div>
  <div class="abs" style="left:280px;top:16px;font-family:'Oswald',sans-serif;font-size:8px;color:var(--orange)">43,000 Cars</div>
  <div class="ph" role="img" aria-label="Balance scale weighing plastic debris against a pile of cars" style="left:196px;top:30px;width:142px;height:62px;background:linear-gradient(#c8d6df,#5e8aa4)"></div>
  <div class="abs" style="left:170px;top:98px;font-family:'Oswald',sans-serif;font-size:8px;color:var(--blue)">Total Foam Plastic Mass</div>
  <div class="abs" style="left:290px;top:98px;font-family:'Oswald',sans-serif;font-size:8px;color:var(--blue)">18 Cars</div>
  <div class="abs" style="left:152px;top:132px;font-family:'Oswald',sans-serif;font-size:19px;color:var(--white);font-weight:600">SIZING IT UP</div>
  <div class="size-row" style="top:162px"><span class="abs" style="left:104px;top:6px">MEGAPLASTICS</span><span class="abs" style="left:262px;top:6px">&gt;50 cm</span></div>
  <div class="size-row" style="top:190px"><span class="abs" style="left:124px;top:6px">MACROPLASTICS</span><span class="abs" style="left:280px;top:6px">5 – 50 cm</span></div>
  <div class="size-row" style="top:218px"><span class="abs" style="left:150px;top:6px">MESOPLASTICS</span><span class="abs" style="left:300px;top:6px">0.5 – 5 cm</span></div>
  <div class="size-row" style="top:246px;border:none"><span class="abs" style="left:172px;top:6px">MICROPLASTICS</span><span class="abs" style="left:320px;top:6px">0.05 – 0.5 cm</span></div>
  <div class="bag" role="img" aria-label="Trash bag, 42 tons" style="left:8px;top:150px;width:50px;height:34px;font-size:9px">42 tons</div>
  <div class="bag" role="img" aria-label="Trash bag, 20 tons" style="left:38px;top:192px;width:44px;height:30px;font-size:7.5px">20 tons</div>
  <div class="bag" role="img" aria-label="Trash bag, 19 tons" style="left:62px;top:228px;width:38px;height:26px;font-size:6.5px">19 tons</div>
  <div class="bag" role="img" aria-label="Trash bag, 0.5 tons" style="left:80px;top:260px;width:32px;height:22px;font-size:5.5px">0,5 tons</div>
</section>

<!-- Mismanaged EPS -->
<section class="panel" style="left:402px;top:606px;width:382px;height:285px">
  <div class="panel-head" style="height:50px;font-size:15px;font-weight:500">How much mismanaged EPS waste was found?</div>
  <div class="ph" role="img" aria-label="World map" style="left:14px;top:60px;width:350px;height:210px;background:radial-gradient(ellipse at center,#ebebeb,#f9f9f9);border-radius:30px"></div>
  <div class="bubble" style="left:20px;top:70px;width:88px;height:88px;background:var(--olive)"><div class="cap">Worldwide Annual<br>Plastics Production</div><div class="val">320,000,000 tons</div></div>
  <div class="bubble" style="left:48px;top:132px;width:88px;height:88px;background:var(--blue)"><div class="cap">Total GPGP Plastics</div><div class="val">78,908 tons</div></div>
  <div class="bubble" style="left:66px;top:188px;width:80px;height:80px;background:var(--gold)"><div class="cap" style="font-size:5.6px">Percent of Global<br>Production in GPGP</div><div class="val" style="font-size:8px">0.000024%</div></div>
  <div class="bubble" style="left:258px;top:62px;width:88px;height:88px;background:var(--olive)"><div class="cap" style="font-size:5.6px">Worldwide Expanded<br>Polystyrene (EPS)<br>Plastics Production</div><div class="val">6,620,000 tons</div></div>
  <div class="bubble" style="left:244px;top:124px;width:90px;height:90px;background:var(--blue)"><div class="cap">Total GPGP<br>Foam Plastics</div><div class="val">35 tons</div></div>
  <div class="bubble" style="left:228px;top:186px;width:80px;height:80px;background:var(--gold)"><div class="cap" style="font-size:5.6px">Percent of Global<br>Production in GPGP</div><div class="val" style="font-size:8px">0.0000053%</div></div>
</section>

<!-- Conclusion -->
<section class="panel" style="left:200px;top:904px;width:382px;height:286px">
  <div class="panel-head" style="height:66px;font-size:27px;font-weight:500">Surprising discoveries</div>
  <div style="padding:20px 18px 0">
    <div class="find"><svg width="18" height="18"><use href="#check"/></svg>Approximately 50% of GPGP Plastics are From Marine-Based Sources.</div>
    <div class="find"><svg width="18" height="18"><use href="#check"/></svg>Beach Litter Studies Were Not Indicative of GPGP Content.</div>
    <div class="find"><svg width="18" height="18"><use href="#check"/></svg>20% of the GPGP Plastic Debris Is From the 2011 Tohoku Tsunami</div>
  </div>
  <div class="abs" style="left:20px;top:176px;width:242px;font-size:8.6px;line-height:1.45">
    <div style="color:var(--blue);font-size:11.5px;font-weight:700;line-height:1.25">All Marine Plastic Debris Is A Problem!</div>
    However, plastic product bans will be ineffective in reducing ocean debris. Since the U.S. contributes just <span class="gold" style="font-size:10.5px">0.9%</span> of the World's Mismanaged Plastic Waste<sup>1</sup>, it is even more important to consider all parts of equation.
    <div style="font-size:4.6px;line-height:1.2;margin-top:1px"><sup>1</sup>Source: <span style="color:var(--blue);text-decoration:underline">6 things you can do to stop plastic pollution today</span>, Daily Ledger, September 7, 2018</div>
  </div>
  <div class="bag" role="img" aria-label="Trash bag labelled just 0.90% of world's mismanaged plastic waste" style="left:268px;top:198px;width:106px;height:78px;flex-direction:column;color:var(--white);font-family:'Carlito',sans-serif;font-size:6px;line-height:1.15;text-align:center">
    <span>just</span>
    <span style="font-family:'Oswald',sans-serif;font-size:15px;color:var(--orange)">0.90%</span>
    <span>World's Mismanaged Plastic<br>Waste</span>
  </div>
</section>
</body>
</html>
```